Flyer for a Business Consultant

I need a one-page description of services. I am a Brennick Certifed Talents Mentor. I do not have a personal website but think I will soon purchase this template https://varlowskins.example/skins/lectern/. I like the larger font, simplicity and larger font. I will attach his pricing flyer which I like - not to overly guide or restrict your creative thinking, but only to give a little perspective. I don't like busy, noisy - I like clarity, simplicity. Here 's the Brennick website which these same traits https://www.brennicktalentshub.example/ and can be a source of ideas and colors.

Target Market(s)

CEOs and Middle Managers in organizations

Industry/Entity Type

Financial Service

Colors

Designer to choose colors to be used in the design.

Requirements
Must have
• Clarity, simplicity, but also strength (not weak or frilly looking)
Nice to have
• Warm color(s), larger/not skinny font
Should not have
• Loud, noisy, busy

```html
<!DOCTYPE html>
<html lang="en">
<head>
<meta charset="utf-8">
<title>A Strength-Based Approach to Managing Team Effectiveness</title>
<link href="https://fonts.googleapis.com/css2?family=Oswald:wght@300;400;600&family=Montserrat:ital,wght@0,300;0,400;0,600;1,700&family=Cormorant+Garamond:wght@500&display=swap" rel="stylesheet">
<style>
  :root {
    --paper: #f3f3f3;
    --ink: #3a3a3a;
    --ink-dark: #222222;
    --accent: #2b7bb0;
    --heading-blue: #2a78a8;
    --band-light: #a9c8d8;
    --band-grey: #a7bcc8;
    --logo-grey: #8a8a8a;
    --icon-grey: #8e8e8e;
  }
  html, body { margin: 0; padding: 0; overflow: hidden; background: var(--paper); }
  .flyer {
    position: relative; width: 849px; height: 1200px; overflow: hidden;
    background: var(--paper); font-family: "Montserrat", sans-serif; color: var(--ink);
  }
  .brand { position: absolute; left: 37px; top: 18px; display: flex; align-items: center; gap: 8px; }
  .brand-mark { width: 36px; height: 38px; background: var(--logo-grey); }
  .brand-name { font-family: "Montserrat", sans-serif; font-weight: 400; color: var(--logo-grey); font-size: 11px; line-height: 1.35; letter-spacing: 0.3px; }
  .brand-name span { display: block; font-size: 17px; letter-spacing: 0; }
  .top-rule { position: absolute; left: 253px; right: 14px; top: 69px; height: 3px; background: var(--accent); }
  .title { position: absolute; right: 32px; top: 88px; text-align: right; font-family: "Oswald", sans-serif; color: var(--ink-dark); margin: 0; }
  .title-lead { display: block; font-weight: 300; font-size: 33px; letter-spacing: 1px; line-height: 40px; }
  .title-main { display: block; font-weight: 600; font-size: 33px; letter-spacing: 1px; line-height: 42px; }
  .intro { position: absolute; left: 44px; top: 205px; margin: 0; font-weight: 400; font-size: 23px; letter-spacing: 3px; color: var(--ink-dark); }
  .intro-rule { position: absolute; left: 38px; top: 243px; width: 56px; height: 3px; background: var(--accent); }
  .benefits { position: absolute; left: 0; top: 260px; width: 849px; height: 148px; }
  .benefit { position: absolute; top: 0; height: 148px; text-align: center; }
  .benefit svg { display: block; margin: 14px auto 0; }
  .benefit p { margin: 12px 0 0; font-size: 14px; line-height: 18px; letter-spacing: 1px; color: var(--ink); }
  .benefit-1 { left: 50px; width: 270px; }
  .benefit-2 { left: 328px; width: 262px; }
  .benefit-3 { left: 598px; width: 240px; }
  .divider { position: absolute; top: 0; width: 4px; height: 148px; background: var(--accent); }
  .divider-1 { left: 323px; }
  .divider-2 { left: 592px; }
  .service { position: absolute; left: 0; width: 849px; }
  .service h2 { margin: 0 0 4px; font-style: italic; font-weight: 700; font-size: 18px; letter-spacing: 1.6px; color: var(--heading-blue); }
  .service p { margin: 0; font-size: 15.3px; line-height: 20.5px; letter-spacing: 1.05px; color: var(--ink); }
  .photo { position: absolute; }
  .service-individual { top: 424px; height: 206px; background: var(--band-light); }
  .service-individual .photo { left: 0; top: 0; width: 226px; height: 206px; background: radial-gradient(circle at 55% 55%, #c9a45a 0%, #6a5230 18%, #2d3038 50%, #1b1f27 100%); }
  .service-individual .copy { position: absolute; left: 263px; top: 28px; width: 566px; }
  .service-workshop { top: 630px; height: 208px; background: var(--band-grey); }
  .service-workshop .photo { right: 0; top: -4px; width: 223px; height: 212px; background: linear-gradient(135deg, #4b4f57 0%, #c2a392 45%, #9aa0a6 70%, #e3e4e6 100%); }
  .service-workshop .copy { position: absolute; left: 26px; top: 18px; width: 590px; text-align: center; }
  .service-followon { top: 838px; height: 209px; background: var(--band-light); }
  .service-followon .photo { left: 0; top: 0; width: 226px; height: 209px; background: linear-gradient(120deg, #2a2422 0%, #6b4a3c 40%, #c99479 70%, #3a302c 100%); }
  .service-followon .copy { position: absolute; left: 263px; top: 20px; width: 566px; }
  .footer-rule { position: absolute; left: 37px; right: 19px; top: 1070px; height: 3px; background: var(--accent); }
  .contact { position: absolute; right: 47px; top: 1093px; text-align: right; font-size: 15.5px; line-height: 21px; letter-spacing: 1.2px; color: var(--ink-dark); }
  .contact strong { font-weight: 600; }
  .contact-bar { position: absolute; left: 812px; top: 1093px; width: 2px; height: 80px; background: var(--ink-dark); }
  .bottom-band { position: absolute; left: 0; right: 0; bottom: 0; height: 6px; background: var(--accent); }
</style>
</head>
<body>
<div class="flyer">
  <div class="brand">
    <div class="brand-mark"></div>
    <div class="brand-name">BRENNICK CERTIFED<span>Talents Mentor</span></div>
  </div>
  <div class="top-rule"></div>

  <h1 class="title">
    <span class="title-lead">A STRENGTH-BASED APPROACH TO</span>
    <span class="title-main">MANAGING TEAM EFFECTIVENESS</span>
  </h1>

  <h2 class="intro">WE HELP TEAMS GROW STRONGER BY:</h2>
  <div class="intro-rule"></div>

  <div class="benefits">
    <div class="benefit benefit-1">
      <svg width="54" height="54" viewBox="0 0 54 54" aria-hidden="true">
        <circle cx="27" cy="27" r="26" fill="var(--icon-grey)"/>
        <path d="M14 38 C16 26 20 18 26 14 L31 17 L27 22 L24 21 C22 26 22 30 26 32 C30 28 36 28 40 32 C38 38 30 41 20 40 Z" fill="#f3f3f3"/>
      </svg>
      <p>Bringing a deep awareness<br>of their strengths and the strengths<br>of their associates.</p>
    </div>
    <div class="divider divider-1"></div>
    <div class="benefit benefit-2">
      <svg width="60" height="54" viewBox="0 0 60 54" aria-hidden="true" fill="var(--icon-grey)">
        <path d="M12 14 V6 H48 V14" fill="none" stroke="var(--icon-grey)" stroke-width="2"/>
        <path d="M9 11 L12 16 L15 11 Z M45 11 L48 16 L51 11 Z"/>
        <circle cx="30" cy="10" r="3"/>
        <circle cx="14" cy="24" r="4.5"/><rect x="8" y="30" width="12" height="20" rx="3"/>
        <circle cx="30" cy="24" r="4.5"/><rect x="24" y="30" width="12" height="20" rx="3"/>
        <circle cx="46" cy="24" r="4.5"/><rect x="40" y="30" width="12" height="20" rx="3"/>
      </svg>
      <p>Increasing the<br>Team's communication<br>and sense of partnership.</p>
    </div>
    <div class="divider divider-2"></div>
    <div class="benefit benefit-3">
      <svg width="56" height="54" viewBox="0 0 56 54" aria-hidden="true" fill="var(--icon-grey)">
        <path d="M20 4 H36 V14 C36 20 32 23 28 23 C24 23 20 20 20 14 Z"/>
        <rect x="26" y="23" width="4" height="5"/><rect x="22" y="28" width="12" height="3"/>
        <path d="M8 18 V8 M5 11 L8 7 L11 11 M48 18 V8 M45 11 L48 7 L51 11" stroke="var(--icon-grey)" stroke-width="2" fill="none"/>
        <rect x="16" y="33" width="24" height="19"/><rect x="4" y="40" width="12" height="12"/><rect x="40" y="40" width="12" height="12"/>
        <circle cx="28" cy="42" r="3.5" fill="#f3f3f3"/>
      </svg>
      <p>Improving<br>employee engagement<br>and effectiveness.</p>
    </div>
  </div>

  <section class="service service-individual">
    <div class="photo" role="img" aria-label="Photo of cupped hands holding a glowing light bulb"></div>
    <div class="copy">
      <h2>INDIVIDUAL SESSIONS</h2>
      <p>Conversational feedback and coaching sessions based on Brennick's TalentCompass assessments. These sessions last about an hour and lead to a personalized translation of the results and how their strengths show up in their work and inherent blind spots they bring.</p>
    </div>
  </section>

  <section class="service service-workshop">
    <div class="copy">
      <h2>STRENGTH DISCOVERY WORKSHOP</h2>
      <p>A retreat-style Team Workshop in which the team learns each other's unique Top 5 strengths. The session is very interactive and provides a common language that leads to improved communication and effectiveness. Tailored in 2,3,and 4-hour options are tailored to your Team's challenges and opportunities.</p>
    </div>
    <div class="photo" role="img" aria-label="Photo of colleagues talking around a table with a laptop"></div>
  </section>

  <section class="service service-followon">
    <div class="photo" role="img" aria-label="Photo of a smiling woman"></div>
    <div class="copy">
      <h2>FOLLOW-ON MODULES</h2>
      <p>Follow-on is important to make the insights learned to be practical and integrated into the Teams' approach and workflows.<br>In a debrief session included as part of the workshop, we provide several 15-minute exercise modules for use in regular meetings, and we offer guest facilitated modules of 30- 60 minutes each.</p>
    </div>
  </section>

  <div class="footer-rule"></div>
  <address class="contact" style="font-style: normal;">
    <strong>Dalia Fenwright</strong><br>
    Brennick Workplace Talents Mentor<br>
    dalia@talentsfocus.example<br>
    555-014-2278
  </address>
  <div class="contact-bar"></div>
  <div class="bottom-band"></div>
</div>
</body>
</html>
```